8x8 Social Media Ad - Harbor Summit Expo

Attention Real Estate Agents
Please join us for our
Quarterly Real Estate Training Expo
The 2nd Saturday of February, May, August and November
Our Next Training Expo is _________________________________
From 9 am to 1 pm
at
Marlowe Suites Fernridge Station
4187 Copperleaf Lane, Greenbelt, MD 20770
Scheduled Speakers
9:00 am - Desmond Pryce - Orientation
9:30 am - Terrell Oakes - Multiple Income Streams / Keystone Track
10:00 am - Lorna Beckett - Marketing though Social Media
10:45 am - Raul Denning - Generating Business through Kelp-Nest
11:30 am - Tunde Adesemi - Real Estate Investing
12:15 pm - Marcus Oyelowo - (Main Speaker) Training Topic TBA
For more information call Desmond Pryce at (240) 555-0192 or email dpryce@harborsummithomes.example

```html
<!DOCTYPE html>
<html lang="en">
<head>
<meta charset="utf-8">
<title>Harbor Summit Expo – Quarterly Real Estate Training Expo</title>
<link href="https://fonts.googleapis.com/css2?family=Barlow:wght@300;400;600;700;800&display=swap" rel="stylesheet">
<style>
  :root {
    --teal: #0f97a3;
    --teal-dark: #0b7f8a;
    --ink: #111111;
    --white: #ffffff;
    --stage: #d2d3d5;
    --photo-a: #6d6a6a;
    --photo-b: #c9c4c0;
  }
  * { margin: 0; padding: 0; box-sizing: border-box; }
  html, body { width: 1200px; height: 1010px; overflow: hidden; background: var(--stage); }
  body { font-family: "Barlow", Arial, sans-serif; position: relative; }

  .ad { position: absolute; left: 199px; top: 105px; width: 802px; height: 802px; background: var(--white); overflow: hidden; }
  .shapes { position: absolute; inset: 0; }

  .brand { position: absolute; left: 30px; top: 58px; display: flex; align-items: center; gap: 12px; }
  .brand-mark { width: 26px; height: 26px; background: var(--teal); }
  .brand-name { color: var(--teal); font-weight: 800; font-size: 27px; line-height: 1.05; text-transform: uppercase; }

  .kicker { position: absolute; left: 352px; top: 29px; color: var(--teal); font-weight: 700; font-size: 25px; letter-spacing: .5px; }
  .invite { position: absolute; left: 352px; top: 64px; color: var(--white); font-weight: 300; font-size: 27px; letter-spacing: .8px; }
  .headline { position: absolute; left: 352px; top: 96px; color: var(--white); font-weight: 700; font-size: 33px; line-height: 35px; letter-spacing: .5px; }

  .section-title { position: absolute; left: 0; width: 802px; top: 190px; text-align: center; font-weight: 700; font-size: 19px; letter-spacing: .6px; color: var(--ink); }

  .photo { position: absolute; border-radius: 50%; border: 4px solid var(--white); background: radial-gradient(circle at 50% 40%, var(--photo-b), var(--photo-a)); }
  .photo.small { width: 106px; height: 106px; }
  .photo.main { width: 226px; height: 226px; left: 566px; top: 245px; background: radial-gradient(circle at 50% 40%, #d9d4cf, #5b5552); }

  .slot { position: absolute; color: var(--ink); }
  .slot .time { color: var(--white); font-weight: 700; font-size: 17px; display: block; margin-bottom: 10px; }
  .slot .name { font-weight: 700; font-size: 16px; display: block; line-height: 18px; }
  .slot .topic { font-size: 15px; line-height: 17px; display: block; }

  .keynote { position: absolute; left: 603px; top: 487px; color: var(--white); }
  .keynote .time { font-weight: 700; font-size: 20px; display: block; }
  .keynote .name { font-weight: 700; font-size: 21px; display: block; line-height: 24px; }
  .keynote .topic { font-size: 18px; line-height: 21px; display: block; }

  .schedule { position: absolute; left: 34px; top: 611px; color: var(--white); font-size: 16px; line-height: 19px; letter-spacing: .3px; text-transform: uppercase; }
  .schedule b { font-weight: 700; }
  .schedule hr { border: 0; border-top: 1px solid var(--white); width: 533px; margin: 7px 0 9px; }

  .contact { position: absolute; left: 32px; top: 732px; color: var(--white); font-size: 20px; line-height: 26px; letter-spacing: .3px; }
  .contact .label { font-weight: 700; display: block; }
  .contact b { font-weight: 700; text-transform: none; }
</style>
</head>
<body>
<main class="ad">
  <svg class="shapes" width="802" height="802" viewBox="0 0 802 802" aria-hidden="true">
    <polygon points="291,0 802,0 802,22 288,22" fill="var(--teal)"/>
    <polygon points="277,58 802,58 802,180 248,180" fill="var(--teal)"/>
    <line x1="0" y1="202" x2="283" y2="202" stroke="var(--ink)" stroke-width="3"/>
    <line x1="518" y1="202" x2="802" y2="202" stroke="var(--ink)" stroke-width="3"/>
    <rect x="0" y="225" width="802" height="370" fill="var(--teal)"/>
    <rect x="70" y="285" width="570" height="60" fill="var(--white)"/>
    <rect x="70" y="395" width="570" height="58" fill="var(--white)"/>
    <rect x="70" y="510" width="570" height="53" fill="var(--white)"/>
    <polygon points="0,603 740,603 740,713 0,713" fill="var(--ink)"/>
    <circle cx="805" cy="485" r="248" fill="var(--teal)" stroke="var(--white)" stroke-width="4"/>
    <rect x="0" y="720" width="802" height="82" fill="var(--teal)"/>
  </svg>

  <div class="brand">
    <span class="brand-mark"></span>
    <span class="brand-name">Harbor Summit<br>Realty Group</span>
  </div>

  <p class="kicker">ATTENTION REAL ESTATE AGENTS</p>
  <p class="invite">PLEASE JOIN US FOR OUR</p>
  <h1 class="headline">QUARTERLY REAL ESTATE<br>TRAINING EXPO</h1>

  <h2 class="section-title">SCHEDULED SPEAKERS</h2>

  <div class="photo small" style="left:14px;top:246px" role="img" aria-label="Portrait photo of Desmond Pryce"></div>
  <div class="photo small" style="left:270px;top:246px" role="img" aria-label="Portrait photo of Terrell Oakes"></div>
  <div class="photo small" style="left:14px;top:359px" role="img" aria-label="Portrait photo of Lorna Beckett"></div>
  <div class="photo small" style="left:270px;top:365px" role="img" aria-label="Portrait photo of Raul Denning"></div>
  <div class="photo small" style="left:14px;top:474px" role="img" aria-label="Portrait photo of Tunde Adesemi"></div>

  <div class="slot" style="left:127px;top:257px"><span class="time">9:00 am</span><span class="name">Desmond Pryce</span><span class="topic">Orientation</span></div>
  <div class="slot" style="left:389px;top:257px"><span class="time">9:30 am</span><span class="name">Terrell Oakes</span><span class="topic">Multiple Income<br>Streams / Keystone Track</span></div>
  <div class="slot" style="left:127px;top:366px"><span class="time">10:00 am</span><span class="name">Lorna Beckett</span><span class="topic">Marketing though<br>Social Media</span></div>
  <div class="slot" style="left:387px;top:366px"><span class="time">10:45 am</span><span class="name">Raul Denning</span><span class="topic">Generating Business<br>through Kelp-Nest</span></div>
  <div class="slot" style="left:133px;top:484px"><span class="time">11:30 am</span><span class="name">Tunde Adesemi</span><span class="topic">Real Estate Investing</span></div>

  <div class="photo main" role="img" aria-label="Portrait photo of main speaker Marcus Oyelowo"></div>
  <div class="keynote"><span class="time">12:15 pm</span><span class="name">Marcus Oyelowo</span><span class="topic">(Main Speaker)</span><span class="topic">Training Topic TBA</span></div>

  <div class="schedule">
    <b>The 2nd Saturday of February, May, August and November</b><br>
    Our next training expo is.
    <hr>
    <b>From 9 am to 1 pm</b> at Marlowe Suites Fernridge Station<br>
    4187 Copperleaf Lane, Greenbelt, MD 20770
  </div>

  <div class="contact">
    <span class="label">FOR MORE INFORMATION CALL</span>
    DESMOND PRYCE at <b>(240) 555-0192</b> or email <b>dpryce@harborsummithomes.example</b>
  </div>
</main>
</body>
</html>
```